Food home delivery flyer to attract new customers and drive web traffic

We need a flyer for Grubella Home Delivery for our door to door leaflet drop. The aim of our marketing is to attract new customers by driving traffic to our website and raise awareness of our service.

We want the flyer in A5, double sided, and in colour. This campaign will be primarily in print, but we need a PDF option also.

Please visit www.grubellahomedelivery.example to obtain a real feel of who we are and what we do.

The flyer should contain the Grubella Home Delivery logo, with our images to compliment our service and what we offer. All are attached to this brief, along with what wording we expect to be included in the flyer.

The main points we need to shout about are:
Sourcing fresh produce from local growers
Partnering with local businesses
Friendly team offering superior customer service
Fast, safe home delivery
Sustainable business

```html
<!DOCTYPE html>
<html lang="en">
<head>
<meta charset="utf-8">
<title>Grubella Home Delivery – A5 Flyer</title>
<link rel="stylesheet" href="https://fonts.googleapis.com/css2?family=Montserrat:wght@500;600;700&family=Open+Sans:wght@400;600;700&family=Oswald:wght@500&family=Roboto:wght@400&display=swap">
<style>
  :root {
    --backdrop: #4b4b4d;
    --green-dark: #17773a;
    --lime: #8dc63f;
    --wood: #2c2e30;
    --ink: #1b1b1b;
    --text: #2e2e2e;
    --white: #ffffff;
  }
  * { box-sizing: border-box; margin: 0; padding: 0; }
  html, body { width: 1200px; height: 900px; overflow: hidden; background: var(--backdrop); }
  .canvas { position: relative; width: 1200px; height: 900px; }

  .flyer { position: absolute; top: 47px; width: 570px; height: 806px; background: var(--white); overflow: hidden; }
  .flyer--front { left: 15px; }
  .flyer--back { left: 615px; }

  .abs { position: absolute; }

  .brand-title { font-family: "Montserrat", sans-serif; font-weight: 700; line-height: 1; white-space: nowrap; }
  .brand-title__name { font-size: 36px; letter-spacing: -0.5px; }
  .brand-title__service { font-size: 37px; letter-spacing: -1px; color: var(--lime); margin-top: 6px; }

  /* Front header */
  .front-header { left: 0; top: 0; width: 570px; height: 328px; background: linear-gradient(90deg, #35383a 0%, var(--wood) 60%, #242628 100%); }
  .front-header__produce { right: 0; top: 0; width: 200px; height: 328px;
    background: radial-gradient(circle at 30% 20%, #c9a36a 0 14%, transparent 15%),
                radial-gradient(circle at 70% 45%, #e3572e 0 12%, transparent 13%),
                radial-gradient(circle at 25% 60%, #6f9a3a 0 16%, transparent 17%),
                linear-gradient(160deg, #b45a2a 0%, #5f8b2f 40%, #7a2d4a 70%, #3f6b2a 100%); }
  .front-header .brand-title { left: 33px; top: 50px; color: var(--white); }
  .front-header__tagline { left: 33px; top: 150px; width: 320px; font-family: "Roboto", sans-serif; font-size: 15.5px; line-height: 20px; color: var(--white); }

  .order-strip { left: 0; top: 236px; width: 350px; height: 60px; background: var(--green-dark); }
  .order-strip__text { left: 33px; top: 6px; font-family: "Montserrat", sans-serif; font-weight: 700; font-size: 13.5px; line-height: 16px; color: var(--white); }
  .order-strip__date { color: var(--lime); }
  .truck-graphic { left: 325px; top: 240px; width: 165px; height: 85px; border-radius: 6px; background: linear-gradient(180deg, #1d8a44, #136b33); }
  .truck-graphic__label { left: 362px; top: 243px; font-family: "Oswald", sans-serif; font-weight: 500; font-style: italic; font-size: 19px; line-height: 20px; color: var(--white); }

  .promise-band { left: 0; top: 328px; width: 570px; height: 116px; background: var(--green-dark); border-bottom: 5px solid var(--lime); }
  .promise-band__text { left: 29px; top: 26px; width: 340px; font-family: "Montserrat", sans-serif; font-weight: 500; font-size: 17.5px; line-height: 21.5px; color: var(--white); }

  .side-panel { background: var(--green-dark); }
  .front-side-panel { left: 395px; top: 449px; width: 175px; height: 285px; clip-path: polygon(20% 0, 100% 0, 100% 100%, 0 100%); }

  .photo-circle { position: absolute; border-radius: 50%; border: 5px solid var(--lime); box-shadow: inset 0 0 0 4px var(--white); }
  .photo--bowls { background: radial-gradient(circle at 60% 40%, #8fb24a 0 18%, transparent 19%), linear-gradient(135deg, #c98b3e, #6e8f3a 50%, #d9c7a2); }
  .photo--pizza { background: radial-gradient(circle at 45% 50%, #d84a2a 0 20%, transparent 21%), linear-gradient(135deg, #e0a54a, #c2402a 55%, #b98a4f); }
  .photo--platter { background: radial-gradient(circle at 50% 50%, #f3efe7 0 30%, transparent 31%), linear-gradient(135deg, #d33b2b, #e8e1d8 50%, #9b3b2f); }

  .about { left: 28px; top: 470px; width: 350px; }
  .about__heading { font-family: "Montserrat", sans-serif; font-weight: 700; font-size: 19px; color: var(--green-dark); padding-bottom: 5px; border-bottom: 1.5px solid var(--green-dark); }
  .about__body { font-family: "Open Sans", sans-serif; font-size: 9.4px; line-height: 11.4px; color: var(--text); margin-top: 14px; }
  .about__body p + p { margin-top: 11px; }
  .about__body strong { font-weight: 700; color: var(--ink); }

  .offer { font-family: "Montserrat", sans-serif; font-weight: 700; font-size: 14px; line-height: 18px; color: var(--green-dark); white-space: nowrap; }
  .offer__pct { color: var(--lime); }
  .flyer--front .offer { left: 28px; top: 663px; }
  .flyer--back .offer { left: 27px; top: 668px; font-size: 12.4px; line-height: 16.5px; }

  /* Footer */
  .footer { left: 0; top: 730px; width: 570px; height: 76px; }
  .footer svg { position: absolute; left: 0; top: 0; }
  .footer__brand { left: 22px; top: 18px; font-family: "Montserrat", sans-serif; font-weight: 600; font-size: 29px; line-height: 1; color: var(--green-dark); }
  .footer__brand-sub { left: 74px; top: 52px; font-family: "Montserrat", sans-serif; font-weight: 600; font-size: 11px; color: var(--green-dark); }
  .footer__cta { left: 218px; top: 14px; font-family: "Montserrat", sans-serif; font-weight: 700; font-size: 12.5px; line-height: 14px; color: var(--white); white-space: nowrap; }
  .footer__cta-accent { color: var(--lime); }
  .footer__phone { left: 370px; top: 10px; display: flex; align-items: center; gap: 6px; white-space: nowrap; font-family: "Oswald", sans-serif; font-weight: 500; font-size: 26px; line-height: 34px; color: var(--white); letter-spacing: 0.3px; }
  .footer__phone .icon, .footer__address .icon { position: static; flex-shrink: 0; }
  .footer__address { left: 214px; top: 56px; display: flex; align-items: center; gap: 4px; font-family: "Montserrat", sans-serif; font-weight: 600; font-size: 7.6px; color: var(--white); white-space: nowrap; }

  /* Back header */
  .back-header .brand-title { left: 33px; top: 37px; color: var(--ink); }
  .back-header__basket { left: 365px; top: 12px; width: 205px; height: 305px; border-radius: 8px;
    background: radial-gradient(circle at 30% 70%, #d6342a 0 14%, transparent 15%),
                radial-gradient(circle at 55% 35%, #8a5a8a 0 12%, transparent 13%),
                linear-gradient(160deg, #4f7f35 0%, #b8874a 45%, #c98f4e 65%, #6a9a3a 100%); }
  .back-header__intro { left: 33px; top: 122px; width: 300px; font-family: "Roboto", sans-serif; font-size: 11.4px; line-height: 14.8px; color: var(--ink); }
  .back-header__intro p + p { margin-top: 14.5px; }

  .gallery-band { left: 0; top: 328px; width: 570px; height: 122px; background: var(--green-dark); border-bottom: 5px solid var(--lime); }

  .points { left: 27px; top: 475px; width: 335px; }
  .points__heading { font-family: "Montserrat", sans-serif; font-weight: 700; font-size: 16.5px; line-height: 18px; color: var(--green-dark); padding-bottom: 6px; border-bottom: 1.5px solid var(--green-dark); width: 290px; }
  .points__list { list-style: none; margin-top: 10px; }
  .points__item { display: flex; align-items: center; gap: 8px; height: 24.5px; white-space: nowrap; border-bottom: 1px solid #e2e2e2; font-family: "Open Sans", sans-serif; font-weight: 600; font-size: 11.6px; letter-spacing: 0.3px; color: var(--ink); }
  .points__item svg { flex-shrink: 0; }
  .points__item:last-child { border-bottom: none; }

  .back-side-panel { left: 330px; top: 455px; width: 240px; height: 279px; clip-path: polygon(35% 0, 100% 0, 100% 100%, 0 100%); }
  .courier-art { left: 368px; top: 455px; width: 195px; height: 280px; border-radius: 10px; background: linear-gradient(160deg, #f3df2c 0%, #e9b27a 35%, #d93a2e 70%, #2d3f8f 100%); opacity: 0.92; }
</style>
</head>
<body>
<main class="canvas">

  <!-- Front side -->
  <section class="flyer flyer--front">
    <div class="abs front-header">
      <div class="abs front-header__produce" role="img" aria-label="Photo of fresh vegetables: potatoes, carrots, beetroot, tomatoes, avocado, broccoli and onions"></div>
      <h1 class="abs brand-title">
        <div class="brand-title__name">GRUBELLA</div>
        <div class="brand-title__service">HOME DELIVERY</div>
      </h1>
      <p class="abs front-header__tagline">Lovingly picked food and produce with provenance Delivered safely to your door by passionate people who care.</p>
    </div>

    <div class="abs order-strip">
      <p class="abs order-strip__text">NOW TAKING ORDERS<br>FOR DELIVERY FROM<br><span class="order-strip__date">WEDNESDAY 8TH JULY</span></p>
    </div>
    <div class="abs truck-graphic" role="img" aria-label="Illustration of a green delivery truck carrying the words food home delivery"></div>
    <p class="abs truck-graphic__label">FOOD HOME<br>DELIVERY</p>

    <div class="abs promise-band">
      <p class="abs promise-band__text">Lovingly picked Kentish food safely delivered from our farm to your home by passionate local people who care.</p>
    </div>

    <div class="abs side-panel front-side-panel"></div>

    <div class="photo-circle photo--bowls" style="left:381px; top:294px; width:180px; height:180px;" role="img" aria-label="Photo of prepared picnic food: salads, scotch eggs and pastries"></div>
    <div class="photo-circle photo--pizza" style="left:395px; top:453px; width:152px; height:152px;" role="img" aria-label="Photo of a tomato and basil pizza"></div>
    <div class="photo-circle photo--platter" style="left:402px; top:580px; width:142px; height:142px;" role="img" aria-label="Photo of a sharing platter with bruschetta, cured meats and tomatoes"></div>

    <article class="abs about">
      <h2 class="about__heading">ABOUT US</h2>
      <div class="about__body">
        <p>Avoid the supermarkets and enjoy a unique and balanced food experience with provenance. Order online at <strong>www.grubellahomedelivery.example</strong> for fast contactless next day delivery.</p>
        <p>Grubella brings you the very best producers and growers from The Garden of England to deliver you a delicious choice for all your dining needs. From fresh produce boxes, handmade picnic boxes, fresh Kentish berry boxes to the finest local beer and wines – we've got it covered.</p>
        <p>Using environmentally conscious practices and minimal packaging, working hand in hand with reduced food miles brings you peace of mind with our efforts for a sustainable future.</p>
      </div>
    </article>

    <p class="abs offer">ENJOY <span class="offer__pct">25% OFF</span> ALL YOUR ORDERS IN JULY<br>ENTER CODE LOCALHARVEST AT THE CHECKOUT</p>

    <footer class="abs footer">
      <svg width="570" height="76" viewBox="0 0 570 76" aria-hidden="true">
        <path d="M205 12 H570 V76 H210 Q212 38 205 12 Z" fill="var(--green-dark)"/>
        <path d="M0 18 Q120 -12 190 20 Q212 38 210 76" fill="none" stroke="var(--lime)" stroke-width="5"/>
      </svg>
      <div class="abs footer__brand">Grubella</div>
      <div class="abs footer__brand-sub">home delivery</div>
      <p class="abs footer__cta">CALL US TODAY FOR<br><span class="footer__cta-accent">A FREE ESTIMATE</span></p>
      <div class="abs footer__phone">
        <svg class="icon" width="26" height="26" viewBox="0 0 26 26" aria-hidden="true"><circle cx="13" cy="13" r="11.5" fill="none" stroke="var(--lime)" stroke-width="2"/><path d="M9 7.5 L11 7 L12.3 10 L11 11.2 Q12.3 13.8 14.8 15 L16 13.7 L19 15 L18.5 17 Q17.5 18.8 15 18 Q9.5 15.8 8 11 Q7.3 8.5 9 7.5 Z" fill="var(--lime)"/></svg>
        <span>01632 960418</span>
      </div>
      <p class="abs footer__address">
        <svg class="icon" width="7" height="9" viewBox="0 0 7 9" aria-hidden="true"><path d="M3.5 0 A3.5 3.5 0 0 1 7 3.5 Q7 5.5 3.5 9 Q0 5.5 0 3.5 A3.5 3.5 0 0 1 3.5 0 Z" fill="var(--lime)"/><circle cx="3.5" cy="3.5" r="1.3" fill="var(--green-dark)"/></svg>
        <span>Brambleford Farm, Orchard Lane, Ashcombe, Kent, KT0 4QX, United Kingdom</span>
      </p>
    </footer>
  </section>

  <!-- Back side -->
  <section class="flyer flyer--back">
    <div class="back-header">
      <div class="abs back-header__basket" role="img" aria-label="Photo of a wicker basket filled with cabbage, broccoli, grapes, carrots, peppers, onion and lemon"></div>
      <h1 class="abs brand-title">
        <div class="brand-title__name">GRUBELLA</div>
        <div class="brand-title__service">HOME DELIVERY</div>
      </h1>
      <div class="abs back-header__intro">
        <p>As a family run, farm-based business, Grubella Ltd has worked as a hub for Kentish growers for the past 15 years, distributing their produce to restaurants, hotels and schools.</p>
        <p>In response to the current situation, we launched our home delivery service to bring a selection of veg box delivery including fruit, vegetables and other essentials direct to your door.</p>
        <p>Fresh, local, sustainable and packed with provenance. We can support you and you can support your local farmers.</p>
      </div>
    </div>

    <div class="abs gallery-band"></div>
    <div class="photo-circle photo--bowls" style="left:33px; top:315px; width:148px; height:148px;" role="img" aria-label="Photo of prepared picnic food: salads, scotch eggs and pastries"></div>
    <div class="photo-circle photo--platter" style="left:210px; top:313px; width:152px; height:152px;" role="img" aria-label="Photo of a sharing platter with bruschetta, cured meats and tomatoes"></div>
    <div class="photo-circle photo--pizza" style="left:389px; top:310px; width:156px; height:156px;" role="img" aria-label="Photo of a tomato and basil pizza"></div>

    <div class="abs side-panel back-side-panel"></div>
    <div class="abs courier-art" role="img" aria-label="Cartoon of a smiling delivery rider on a red scooter giving a thumbs up, with a yellow speech bubble reading free delivery"></div>

    <section class="abs points">
      <h2 class="points__heading">THE MAIN POINTS<br>WE NEED TO SHOUT ABOUT ARE:</h2>
      <ul class="points__list">
        <li class="points__item"><svg width="12" height="12" viewBox="0 0 12 12" aria-hidden="true"><circle cx="6" cy="6.5" r="5.2" fill="var(--lime)"/></svg>Sourcing fresh produce from local growers</li>
        <li class="points__item"><svg width="12" height="12" viewBox="0 0 12 12" aria-hidden="true"><circle cx="6" cy="6.5" r="5.2" fill="var(--lime)"/></svg>Partnering with local businesses</li>
        <li class="points__item"><svg width="12" height="12" viewBox="0 0 12 12" aria-hidden="true"><circle cx="6" cy="6.5" r="5.2" fill="var(--lime)"/></svg>Friendly team offering superior customer service</li>
        <li class="points__item"><svg width="12" height="12" viewBox="0 0 12 12" aria-hidden="true"><circle cx="6" cy="6.5" r="5.2" fill="var(--lime)"/></svg>Fast, safe home delivery</li>
        <li class="points__item"><svg width="12" height="12" viewBox="0 0 12 12" aria-hidden="true"><circle cx="6" cy="6.5" r="5.2" fill="var(--lime)"/></svg>Sustainable business</li>
      </ul>
    </section>

    <p class="abs offer">ENJOY <span class="offer__pct">25% OFF</span> ALL YOUR ORDERS IN JULY<br>ENTER CODE LOCALHARVEST AT THE CHECKOUT</p>

    <footer class="abs footer">
      <svg width="570" height="76" viewBox="0 0 570 76" aria-hidden="true">
        <path d="M205 12 H570 V76 H210 Q212 38 205 12 Z" fill="var(--green-dark)"/>
        <path d="M0 18 Q120 -12 190 20 Q212 38 210 76" fill="none" stroke="var(--lime)" stroke-width="5"/>
      </svg>
      <div class="abs footer__brand">Grubella</div>
      <div class="abs footer__brand-sub">home delivery</div>
      <p class="abs footer__cta">CALL US TODAY FOR<br><span class="footer__cta-accent">A FREE ESTIMATE</span></p>
      <div class="abs footer__phone">
        <svg class="icon" width="26" height="26" viewBox="0 0 26 26" aria-hidden="true"><circle cx="13" cy="13" r="11.5" fill="none" stroke="var(--lime)" stroke-width="2"/><path d="M9 7.5 L11 7 L12.3 10 L11 11.2 Q12.3 13.8 14.8 15 L16 13.7 L19 15 L18.5 17 Q17.5 18.8 15 18 Q9.5 15.8 8 11 Q7.3 8.5 9 7.5 Z" fill="var(--lime)"/></svg>
        <span>01632 960418</span>
      </div>
      <p class="abs footer__address">
        <svg class="icon" width="7" height="9" viewBox="0 0 7 9" aria-hidden="true"><path d="M3.5 0 A3.5 3.5 0 0 1 7 3.5 Q7 5.5 3.5 9 Q0 5.5 0 3.5 A3.5 3.5 0 0 1 3.5 0 Z" fill="var(--lime)"/><circle cx="3.5" cy="3.5" r="1.3" fill="var(--green-dark)"/></svg>
        <span>Brambleford Farm, Orchard Lane, Ashcombe, Kent, KT0 4QX, United Kingdom</span>
      </p>
    </footer>
  </section>

</main>
</body>
</html>
```